business card design for luxurious real estate brand

using the attached logo, i am looking for a 2-sided business card design. the back should be the gold logo on black background. the front needs to include: gold logo, name, phone, email, and website

Industry/Entity Type

real estate

Contact Information for Business Card

logo, name, email, phone, website

Font styles to use
Sans Serif

```html
<!DOCTYPE html>
<html lang="en">
<head>
<meta charset="UTF-8">
<title>Casa Verano — Business Card</title>
<link href="https://fonts.googleapis.com/css2?family=Montserrat:wght@300;400;600;700&display=swap" rel="stylesheet">
<style>
  :root {
    --backdrop: #1c1c1d;
    --card-light: #4a474a;
    --card-dark: #2a282a;
    --gold: #f2cd1a;
    --ink-light: #f1f0f0;
  }
  * { margin: 0; padding: 0; box-sizing: border-box; }
  html, body {
    width: 1200px;
    height: 1200px;
    overflow: hidden;
    background: var(--backdrop);
    font-family: "Montserrat", sans-serif;
  }
  .canvas {
    width: 1200px;
    height: 1200px;
    display: flex;
    flex-direction: column;
    align-items: center;
    justify-content: center;
    gap: 80px;
  }
  .card {
    width: 700px;
    height: 400px;
    position: relative;
    background: radial-gradient(ellipse at 50% 45%, var(--card-light) 0%, var(--card-dark) 85%);
    box-shadow: 0 18px 40px rgba(0, 0, 0, 0.55);
  }
  /* Logo side */
  .card--logo {
    display: flex;
    align-items: center;
    justify-content: center;
  }
  .brand {
    display: flex;
    align-items: center;
    gap: 18px;
  }
  .brand__mark {
    width: 22px;
    height: 22px;
    background: var(--gold);
  }
  .brand__name {
    color: var(--gold);
    font-weight: 400;
    font-size: 34px;
    letter-spacing: 0.32em;
    text-transform: uppercase;
  }
  /* Contact side */
  .card--contact {
    display: flex;
    align-items: center;
    padding-left: 90px;
  }
  .identity {
    text-align: left;
  }
  .identity__name {
    color: var(--gold);
    font-weight: 700;
    font-size: 30px;
    line-height: 1.1;
  }
  .identity__title {
    color: var(--ink-light);
    font-weight: 300;
    font-size: 15px;
    margin-top: 8px;
  }
  .divider {
    width: 2px;
    height: 80px;
    background: var(--gold);
    margin: 0 34px 0 36px;
  }
  .contacts {
    list-style: none;
    display: flex;
    flex-direction: column;
    gap: 9px;
  }
  .contacts__item {
    display: flex;
    align-items: center;
    gap: 10px;
    color: var(--ink-light);
    font-size: 16px;
    font-weight: 400;
  }
  .contacts__icon {
    width: 15px;
    height: 15px;
    flex: none;
  }
</style>
</head>
<body>
  <main class="canvas">
    <section class="card card--logo" aria-label="Card back">
      <div class="brand">
        <span class="brand__mark"></span>
        <span class="brand__name">Casa Verano</span>
      </div>
    </section>

    <section class="card card--contact" aria-label="Card front">
      <div class="identity">
        <h1 class="identity__name">Marcus Vale</h1>
        <p class="identity__title">Founder &amp; Director</p>
      </div>
      <span class="divider"></span>
      <ul class="contacts">
        <li class="contacts__item">
          <svg class="contacts__icon" viewBox="0 0 24 24" aria-hidden="true">
            <path fill="#f2cd1a" d="M6.6 10.8a15.1 15.1 0 0 0 6.6 6.6l2.2-2.2c.3-.3.7-.4 1-.2 1.1.4 2.3.6 3.6.6.6 0 1 .4 1 1V20c0 .6-.4 1-1 1A17 17 0 0 1 3 4c0-.6.4-1 1-1h3.5c.6 0 1 .4 1 1 0 1.3.2 2.5.6 3.6.1.3 0 .7-.2 1z"/>
          </svg>
          (555)-014-2290
        </li>
        <li class="contacts__item">
          <svg class="contacts__icon" viewBox="0 0 24 24" aria-hidden="true">
            <rect x="2" y="5" width="20" height="14" rx="1.5" fill="#f2cd1a"/>
            <path d="M3 6.5l9 6.5 9-6.5" fill="none" stroke="#2e2c2e" stroke-width="1.8"/>
          </svg>
          marcus@casaverano.com
        </li>
        <li class="contacts__item">
          <svg class="contacts__icon" viewBox="0 0 24 24" aria-hidden="true">
            <circle cx="12" cy="12" r="10" fill="#f2cd1a"/>
            <g fill="none" stroke="#2e2c2e" stroke-width="1.4">
              <ellipse cx="12" cy="12" rx="4.2" ry="10"/>
              <path d="M2 12h20M4 7h16M4 17h16"/>
            </g>
          </svg>
          www.casaverano.com
        </li>
      </ul>
    </section>
  </main>
</body>
</html>
```